Oil and Gas Letterhead Design Tweak

Simple letterhead information and design tweak.

Please note, we don't want to change the design or logo of the letterhead only the small changes mentioned below.

We need to change the company name up top to "Northvale Petrotek FZCO"

Also, we need to include in the footer the following information. I have attached an image of roughly how we would like to have it displayed in the footer.

Footer Details:

Northvale Petrotek FZCO,
Unit No. 2378, FZCO Trade Hub, level No. 1, K&P 7, Dubai, United Arab Emirates
Northvale Petrotek FZCO is registered as a free zone company under the rules & regulations of FZCO

Target Market(s)

O&G Market

Industry/Entity Type

Oil And Gas

Font styles to use
Sans Serif

Colors

Designer to choose colors to be used in the design.

Requirements
Must have
• Change the company name to Northvale Petrotek FZCO
• Include the footer on the bottom of the first and continuation page
Should not have
• Should not change the design or logo of the letterhead, only the specified changes mentioned above

```html
<!DOCTYPE html>
<html lang="en">
<head>
<meta charset="utf-8">
<title>Northvale Petrotek FZCO – Letterhead</title>
<link href="https://fonts.googleapis.com/css2?family=Montserrat:wght@400;600;700&display=swap" rel="stylesheet">
<style>
  :root {
    --brand-blue: #1b5aa8;
    --brand-red: #e6232e;
    --ink: #2a2a2a;
    --ink-dark: #1a1a1a;
    --paper: #ffffff;
  }
  html, body {
    margin: 0;
    padding: 0;
    width: 848px;
    height: 1200px;
    overflow: hidden;
    background: var(--paper);
  }
  .letterhead {
    position: relative;
    width: 848px;
    height: 1200px;
    background: var(--paper);
    font-family: "Montserrat", Arial, sans-serif;
    color: var(--ink);
  }
  .top-bands, .bottom-bands {
    position: absolute;
    left: 0;
    width: 848px;
  }
  .top-bands { top: 0; height: 15px; }
  .bottom-bands { bottom: 0; height: 20px; }
  .band-blue { fill: var(--brand-blue); }
  .band-red { fill: var(--brand-red); }

  .brand {
    position: absolute;
    top: 44px;
    left: 232px;
    display: flex;
    align-items: center;
    gap: 14px;
  }
  .brand-mark {
    width: 18px;
    height: 18px;
    background: var(--brand-blue);
  }
  .brand-name {
    font-weight: 700;
    font-size: 20px;
    letter-spacing: 0.2px;
    color: var(--ink-dark);
    white-space: nowrap;
  }

  .footer {
    position: absolute;
    left: 0;
    right: 0;
    top: 1112px;
    text-align: center;
  }
  .footer-company {
    margin: 0;
    font-weight: 700;
    font-size: 10.5px;
    letter-spacing: 1.6px;
    text-transform: uppercase;
    color: var(--ink-dark);
  }
  .footer-line {
    margin: 6px 0 0;
    font-weight: 400;
    font-size: 10px;
    color: var(--ink);
  }
</style>
</head>
<body>
  <div class="letterhead">
    <svg class="top-bands" viewBox="0 0 848 15" aria-hidden="true">
      <polygon class="band-blue" points="0,0 193,0 182,15 0,15"/>
      <polygon class="band-red" points="266,0 848,0 848,15 277,15"/>
    </svg>

    <header class="brand">
      <span class="brand-mark" aria-hidden="true"></span>
      <span class="brand-name">NORTHVALE PETROTEK FZCO</span>
    </header>

    <footer class="footer">
      <p class="footer-company">Northvale Petrotek FZCO,</p>
      <p class="footer-line">Unit No. 2378, FZCO Trade Hub, level No. 1, K&amp;P 7, Dubai, United Arab Emirates</p>
      <p class="footer-line">Northvale Petrotek FZCO is registered as a free zone company under the rules &amp; regulations of FZCO</p>
    </footer>

    <svg class="bottom-bands" viewBox="0 0 848 20" aria-hidden="true">
      <polygon class="band-blue" points="587,20 600,0 657,0 644,20"/>
      <polygon class="band-red" points="652,20 665,0 702,0 702,20"/>
    </svg>
  </div>
</body>
</html>
```